Postcard Design for a book promotion

I have written a book which I want to market, and promo. The postcard is an advertisement for promotional purposes. The book is titled "Iron Orchard." By T.J. Havel. I have a website: http://ironorchard.info. I can upload graphics, photos or details.

The story is about a Waist Gunner and Crew 472 of the 517th Bomb Squadron who flew and fought over Germany in World War II.

All of the crew survived.

T J Havel, on Facebook and http://ironorchard. info

Promo

```html
<!DOCTYPE html>
<html lang="en">
<head>
<meta charset="utf-8">
<title>Iron Orchard – Promotional Postcard</title>
<link href="https://fonts.googleapis.com/css2?family=Great+Vibes&family=Tinos:ital,wght@0,400;0,700;1,400&family=Arimo:wght@700&display=swap" rel="stylesheet">
<style>
  :root {
    --page: #eeeeee;
    --ink: #000000;
    --paper: #ffffff;
    --accent: #f2e01e;
    --photo-light: #cfcfcf;
    --photo-dark: #3a3a3a;
    --muted: #8a8a8a;
    --line: #b5b5b5;
  }
  * { box-sizing: border-box; margin: 0; padding: 0; }
  html, body { width: 857px; height: 1200px; overflow: hidden; background: var(--page); }
  .card {
    position: absolute; left: 58px; width: 740px;
    background: var(--paper); overflow: hidden;
    box-shadow: 0 3px 10px rgba(0,0,0,.35);
    font-family: "Tinos", serif;
  }
  .card--front { top: 14px; height: 620px; background: var(--ink); }
  .card--back { top: 652px; height: 534px; }
  .abs { position: absolute; white-space: nowrap; }
  .wrap { white-space: normal; }

  .hero-photo {
    left: 0; top: 0; width: 740px; height: 360px;
    background: linear-gradient(160deg, var(--photo-light) 0%, #9a9a9a 40%, var(--photo-dark) 100%);
  }
  .site-url { font-size: 15px; line-height: 1; color: var(--paper); }

  .book {
    background: var(--paper); box-shadow: 3px 4px 10px rgba(0,0,0,.55);
    text-align: center; color: var(--ink);
  }
  .book__title { font-size: 26px; margin-top: 30px; }
  .book__sub { font-size: 8px; line-height: 1.3; margin: 10px 16px 0; }
  .book__art { margin: 12px auto 0; background: linear-gradient(180deg, #bdbdbd, #5a5a5a); }
  .book__author { font-size: 11px; margin-top: 14px; }

  .portrait {
    border: 4px solid var(--paper);
    background: linear-gradient(180deg, #8a7560, #3b3129);
  }
  .caption { color: var(--paper); font-size: 14px; line-height: 1.2; text-align: center; }

  .kicker-you { font-family: "Great Vibes", cursive; font-size: 58px; line-height: 1; }
  .kicker-line { font-size: 24px; line-height: 1; }
  .title-line { font-family: "Arimo", sans-serif; font-weight: 700; letter-spacing: .5px; line-height: 1; }
  .on-dark { color: var(--paper); }
  .on-light { color: var(--ink); }
  .front-title { color: var(--accent); font-size: 27px; }
  .front-title .byline { font-family: "Great Vibes", cursive; font-weight: 400; font-size: 30px; }
  .blurb { color: var(--paper); font-size: 14.5px; line-height: 1.35; }
  .back-title { color: var(--ink); font-size: 33px; }
  .stamp-box {
    border: 1px solid var(--line); color: var(--muted);
    font-family: "Arimo", sans-serif; font-weight: 700; font-size: 12px;
    display: flex; align-items: center; justify-content: center; text-align: center; line-height: 1.3;
  }
  .address-line { height: 1px; background: var(--line); }
</style>
</head>
<body>

<section class="card card--front" aria-label="Postcard front">
  <div class="abs hero-photo" role="img" aria-label="Black and white photograph of bombers in flight"></div>
  <svg class="abs" style="left:0;top:330px" width="740" height="290" viewBox="0 0 740 290" aria-hidden="true">
    <polygon fill="#000" points="0,30 30,22 60,34 95,18 130,30 170,20 210,34 250,16 290,28 330,20 370,32 410,18 450,30 490,22 530,34 570,18 610,30 650,20 690,32 740,22 740,290 0,290"/>
  </svg>
  <div class="abs site-url" style="left:24px;top:308px">http://ironorchard.info</div>

  <div class="abs book" style="left:530px;top:90px;width:186px;height:290px">
    <div class="book__title">Iron Orchard</div>
    <div class="book__sub wrap">The true story of a bomber crew over Germany</div>
    <div class="book__art" role="img" aria-label="Cover photograph of bombers in the sky" style="width:150px;height:120px"></div>
    <div class="book__author">T.J. Havel</div>
  </div>

  <div class="abs portrait" role="img" aria-label="Portrait photograph of the author" style="left:26px;top:412px;width:96px;height:106px"></div>
  <div class="abs caption" style="left:20px;top:528px;width:108px">T.J. Havel</div>

  <div class="abs kicker-you on-dark" style="left:142px;top:376px">YOU</div>
  <div class="abs kicker-line on-dark" style="left:142px;top:440px">can't afford to Miss EITHER!</div>
  <div class="abs title-line front-title" style="left:142px;top:474px">“IRON ORCHARD” <span class="byline">by T.J. Havel</span></div>
  <p class="abs blurb wrap" style="left:142px;top:518px;width:370px">The story is about a Waist Gunner and Crew 472 of the 517th Bomb Squadron who flew and fought over Germany in World War II.</p>
</section>

<section class="card card--back" aria-label="Postcard back">
  <div class="abs kicker-you on-light" style="left:26px;top:14px">YOU</div>
  <div class="abs kicker-line on-light" style="left:26px;top:78px">can't afford to Miss EITHER!</div>
  <div class="abs title-line back-title" style="left:26px;top:110px">“IRON ORCHARD”</div>

  <div class="abs stamp-box" style="left:612px;top:24px;width:100px;height:104px">Place<br>Stamp<br>Here</div>

  <svg class="abs" style="left:0;top:166px" width="372" height="368" viewBox="0 0 372 368" aria-hidden="true">
    <polygon fill="#000" points="0,22 25,14 55,26 85,10 115,24 150,12 185,26 220,10 255,22 290,12 325,24 372,16 372,368 0,368"/>
  </svg>
  <p class="abs blurb wrap" style="left:26px;top:214px;width:320px;font-size:13.5px">This tribute is about the men who courageously flew and fought in peril, half frozen, suspended in the air five miles above the ground. The men of Crew 472 were more than ordinary men, they were extraordinary men doing an extraordinary job.</p>

  <div class="abs portrait" role="img" aria-label="Portrait photograph of the author" style="left:40px;top:372px;width:82px;height:90px"></div>
  <div class="abs caption" style="left:24px;top:472px;width:114px">Author<br>T.J. Havel</div>

  <div class="abs book" style="left:200px;top:356px;width:112px;height:148px">
    <div class="book__title" style="font-size:15px;margin-top:12px">Iron Orchard</div>
    <div class="book__art" role="img" aria-label="Cover photograph of bombers in the sky" style="width:88px;height:66px;margin-top:10px"></div>
    <div class="book__author" style="font-size:8px;margin-top:10px">T.J. Havel</div>
  </div>
  <div class="abs site-url" style="left:190px;top:512px;font-size:12px">http://ironorchard.info</div>

  <div class="abs address-line" style="left:440px;top:290px;width:270px"></div>
  <div class="abs address-line" style="left:440px;top:340px;width:270px"></div>
  <div class="abs address-line" style="left:440px;top:390px;width:270px"></div>
  <div class="abs address-line" style="left:440px;top:440px;width:270px"></div>
</section>

</body>
</html>
```